Now Leasing Banner

Looking for a banner that says the following information approx 4' x 30'

Now Leasing Maple Ridge Court 925-318-6042

Target Market(s)

Drive by traffic

Industry/Entity Type

Residential property management

Requirements
Must have
• Clear and readable from a distance

```html
<!DOCTYPE html>
<html lang="en">
<head>
<meta charset="utf-8">
<title>Now Leasing Banner – Maple Ridge Court</title>
<link rel="stylesheet" href="https://fonts.googleapis.com/css2?family=Poppins:ital,wght@1,700&family=Roboto:ital,wght@1,900&display=swap">
<style>
  :root {
    --page-bg: #e1e1e1;
    --navy-deep: #03091f;
    --navy: #0a1a55;
    --navy-bright: #10297a;
    --red: #c0080a;
    --red-dark: #8f0506;
    --silver-top: #ffffff;
    --silver-bottom: #a9a9b0;
    --gold-light: #fff4b0;
    --gold: #e2c25a;
    --gold-dark: #a77a22;
    --sky: #e9b979;
    --land: #4f7a3e;
  }
  * { margin: 0; padding: 0; box-sizing: border-box; }
  html, body {
    width: 1200px;
    height: 1200px;
    overflow: hidden;
    background: var(--page-bg);
  }
  .canvas {
    position: relative;
    width: 1200px;
    height: 1200px;
  }
  .banner {
    position: absolute;
    left: 0;
    top: 520px;
    width: 1200px;
    height: 160px;
    overflow: hidden;
  }
  .banner-shapes {
    position: absolute;
    inset: 0;
    width: 1200px;
    height: 160px;
  }
  .headline {
    position: absolute;
    left: 90px;
    top: 22px;
    font-family: "Poppins", sans-serif;
    font-style: italic;
    font-weight: 700;
    font-size: 39px;
    line-height: 1;
    letter-spacing: -0.3px;
    white-space: nowrap;
    background: linear-gradient(180deg, var(--silver-top) 35%, var(--silver-bottom) 100%);
    -webkit-background-clip: text;
    background-clip: text;
    color: transparent;
    filter: drop-shadow(0 2px 3px rgba(0,0,0,0.7));
  }
  .phone {
    position: absolute;
    left: 150px;
    top: 66px;
    font-family: "Roboto", sans-serif;
    font-style: italic;
    font-weight: 900;
    font-size: 66px;
    line-height: 1;
    white-space: nowrap;
    background: linear-gradient(180deg, var(--gold-light) 10%, var(--gold) 55%, var(--gold-dark) 100%);
    -webkit-background-clip: text;
    background-clip: text;
    color: transparent;
    filter: drop-shadow(0 3px 4px rgba(0,0,0,0.75));
  }
</style>
</head>
<body>
<div class="canvas">
  <section class="banner">
    <svg class="banner-shapes" viewBox="0 0 1200 160" xmlns="http://www.w3.org/2000/svg">
      <defs>
        <linearGradient id="navyField" x1="0" y1="0" x2="1" y2="0">
          <stop offset="0" stop-color="var(--navy-deep)"/>
          <stop offset="0.45" stop-color="var(--navy)"/>
          <stop offset="1" stop-color="var(--navy-bright)"/>
        </linearGradient>
        <linearGradient id="propertyScene" x1="0" y1="0" x2="0" y2="1">
          <stop offset="0" stop-color="var(--sky)"/>
          <stop offset="0.4" stop-color="#b7a585"/>
          <stop offset="0.65" stop-color="var(--land)"/>
          <stop offset="1" stop-color="#2f4a26"/>
        </linearGradient>
      </defs>
      <rect class="field" x="0" y="0" width="1200" height="160" fill="url(#navyField)"/>
      <polygon class="corner-accent" points="0,0 81,0 0,82" fill="var(--red)"/>
      <polygon class="diagonal-band" points="842,0 947,0 788,160 683,160" fill="var(--red)"/>
      <polygon class="diagonal-band-shade" points="842,0 858,0 699,160 683,160" fill="var(--red-dark)" opacity="0.5"/>
      <polygon class="accent-triangle" points="788,160 870,80 922,160" fill="var(--navy)"/>
      <polygon class="property-photo" role="img" aria-label="Aerial view of the residential tower and green surroundings at sunset"
               points="947,0 1200,0 1200,160 922,160 870,80" fill="url(#propertyScene)"/>
    </svg>
    <h1 class="headline">NOW LEASING MAPLE RIDGE COURT</h1>
    <p class="phone">925-318-6042</p>
  </section>
</div>
</body>
</html>
```